Recruitment process infographic

We are a boutique recruitment firm and we work remotely, connecting our candidates (mostly non-Japanese engineers) to exciting companies in Japan.
We have multiple steps in the process from scouting candidates on TalentNest, reviewing their CV, helping them prepare for their interview etc. As there are multiple reps involved in each step of the progress, we'd like to prepare an infographic to help our candidates understand the flow of our process, answer their FAQs as well as sharing "who is who".
It should be a clean and clear representation of the candidate journey with our company, to make them feel comfortable knowing they are in safe hands. We welcome any recommendation in wording/format changes to make the process easier / cleaner to understand.
The end product should be on a platform where I can easily add/edit wording, as we need to keep our employee names updated whenever we hire someone new, or something in our process changes.
Here is the wording required. Company name and employee names have not been included at this stage.
https://files.quillmarsh.net/document/d/8vXpLm2TqRw4ZbNk7HyUe3JcFs9DaGtPo5VnQrL-zWxy/edit
The infographic is required for the first page of the document, however we will need a second page (or more) for the FAQs so would be great to see a design that can accommodate that.
Branding/design guidelines:
A minimalistic, clean and clear look
Contrast with the logo (logo is orange on white background)
Icons / images will be great, just as long as they don't clutter the graphic
Process should build trust and inspire confidence
Meant to attracts followers/subscribers
Allows us to smoothly introduce our services/platforms
Typeface: Arial if possible, but open for other clean alternatives
Colours: see attachment
Engineers looking for jobs
Recruitment, IT

```html
<!DOCTYPE html>
<html lang="en">
<head>
<meta charset="utf-8">
<title>Our Process – Recruitment Infographic</title>
<link href="https://fonts.googleapis.com/css2?family=Poppins:wght@600;700&family=Roboto:ital,wght@0,400;0,500;0,700;1,500&display=swap" rel="stylesheet">
<style>
  :root{
    --bg:#cfcfcf;
    --paper:#ececee;
    --navy:#1b1f4b;
    --ink:#141414;
    --orange:#d4511a;
    --muted:#c9c9cf;
    --violet:#4b4a9a;
  }
  html,body{margin:0;padding:0;width:1200px;height:1068px;overflow:hidden;background:var(--bg);}
  .sheet{position:absolute;left:20px;top:128px;width:1160px;height:812px;background:var(--paper);overflow:hidden;
    font-family:Roboto,Arial,sans-serif;color:var(--ink);}
  .abs{position:absolute;}
  .page-title{left:61px;top:64px;margin:0;font-family:Poppins,Arial,sans-serif;font-weight:700;font-size:34px;line-height:42px;letter-spacing:7px;color:#111;z-index:2;}
  .brand{left:390px;top:48px;margin:0;font-family:Poppins,Arial,sans-serif;font-weight:700;font-size:27px;color:var(--navy);letter-spacing:-0.3px;}
  .intro{left:390px;top:100px;width:340px;font-size:13.5px;font-weight:500;line-height:18px;}
  .intro p{margin:0 0 17px;}
  .timeline{left:0;top:0;width:1160px;height:812px;}
  .step-icon{position:absolute;width:48px;height:48px;border-radius:50%;background:var(--orange);display:flex;align-items:center;justify-content:center;}
  .step-title{position:absolute;margin:0;font-family:Roboto,Arial,sans-serif;font-weight:700;font-size:14.5px;line-height:18px;text-transform:uppercase;letter-spacing:-0.2px;}
  .step-title .lower{text-transform:none;}
  .step-body{position:absolute;width:165px;font-size:11px;line-height:13.4px;z-index:2;}
  .step-body p{margin:0 0 13px;}
  .team{position:absolute;width:165px;font-size:11px;line-height:13.4px;z-index:2;}
  .team b{font-weight:700;}
  .outcome-lead{color:var(--orange);font-weight:700;font-size:11px;margin:0 0 12px;}
  .tip{position:absolute;display:flex;flex-direction:column;gap:6px;z-index:2;}
  .tip-badge{width:34px;height:28px;}
  .tip-text{font-style:italic;font-weight:500;font-size:11px;line-height:13.4px;}
  .illustration{position:absolute;border-radius:6px;z-index:0;}
  .bottom-band{left:0;bottom:0;width:1160px;height:9px;background:var(--orange);}
</style>
</head>
<body>
<main class="sheet">

  <div class="illustration" role="img" aria-label="Faint large leaf decoration behind the title" style="left:45px;top:30px;width:270px;height:240px;border-radius:50% 50% 40% 40%;background:radial-gradient(ellipse at center,#e2e2e6,#ececee 70%);"></div>

  <h1 class="abs page-title">OUR<br>PROCESS</h1>
  <h2 class="abs brand">XX company name/logo</h2>
  <div class="abs intro">
    <p>Hi! We are here to help you find your next amazing working opportunity.</p>
    <p>We have an international team of experts that will be guiding and supporting you throughout the process.</p>
  </div>

  <div class="illustration" role="img" aria-label="Illustration of a person presenting a line chart on a whiteboard" style="left:824px;top:46px;width:269px;height:195px;background:linear-gradient(135deg,#dfdfe4,#e6e6ea);"></div>

  <svg class="abs timeline" viewBox="0 0 1160 812" aria-hidden="true">
    <g fill="none" stroke="var(--navy)" stroke-width="2.5">
      <path d="M107 256 H988 Q1003 256 1003 272 V325"/>
      <path d="M943 360 V325 H1065 V360"/>
    </g>
    <circle cx="1003" cy="325" r="7" fill="var(--navy)"/>
    <g fill="var(--orange)">
      <path d="M997 276 h12 l-6 6z"/><path d="M997 285 h12 l-6 6z"/><path d="M997 294 h12 l-6 6z"/>
    </g>
    <g fill="var(--navy)">
      <path d="M387 269 l8 6 l-8 6z"/><path d="M397 269 l8 6 l-8 6z"/><path d="M407 269 l8 6 l-8 6z"/>
      <path d="M852 262 l8 6 l-8 6z"/><path d="M862 262 l8 6 l-8 6z"/><path d="M872 262 l8 6 l-8 6z"/>
    </g>
    <g fill="#dcdce1">
      <path d="M176 226 l7 6 l-7 6z"/><path d="M185 226 l7 6 l-7 6z"/><path d="M194 226 l7 6 l-7 6z"/>
    </g>
  </svg>

  <!-- Step icons -->
  <div class="step-icon" style="left:59px;top:232px;">
    <svg width="26" height="24" viewBox="0 0 26 24" fill="none" stroke="#fff" stroke-width="2.2"><rect x="2" y="2" width="22" height="14" rx="1.5"/><path d="M13 16v4M8 21h10"/></svg>
  </div>
  <div class="step-icon" style="left:273px;top:232px;">
    <svg width="24" height="24" viewBox="0 0 24 24" fill="none" stroke="#fff" stroke-width="2.2" stroke-linecap="round"><path d="M5 3h4l2 5-3 2a12 12 0 0 0 6 6l2-3 5 2v4a2 2 0 0 1-2 2A17 17 0 0 1 3 5a2 2 0 0 1 2-2z"/><path d="M15 3a6 6 0 0 1 6 6M15 7a2 2 0 0 1 2 2"/></svg>
  </div>
  <div class="step-icon" style="left:481px;top:232px;">
    <svg width="26" height="18" viewBox="0 0 26 18" fill="none" stroke="#fff" stroke-width="2.4"><rect x="2" y="2" width="22" height="14" rx="7"/><circle cx="9" cy="9" r="3" fill="#fff"/></svg>
  </div>
  <div class="step-icon" style="left:692px;top:232px;">
    <svg width="24" height="26" viewBox="0 0 24 26" fill="none" stroke="#fff" stroke-width="2.2"><circle cx="12" cy="8" r="5"/><path d="M3 24v-2a7 7 0 0 1 7-7h4a7 7 0 0 1 7 7v2z"/></svg>
  </div>
  <div class="step-icon" style="left:919px;top:360px;">
    <svg width="24" height="24" viewBox="0 0 24 24" fill="#fff"><path d="M2 10h5v12H2zM9 22V10l5-8c2 0 3 1.5 2.5 3.5L15 9h5.5a2 2 0 0 1 2 2.4l-1.8 8.6a2.5 2.5 0 0 1-2.5 2z"/></svg>
  </div>
  <div class="step-icon" style="left:1041px;top:360px;">
    <svg width="24" height="24" viewBox="0 0 24 24" fill="#fff"><path d="M2 2h5v12H2zM9 2v12l5 8c2 0 3-1.5 2.5-3.5L15 15h5.5a2 2 0 0 0 2-2.4L20.7 4a2.5 2.5 0 0 0-2.5-2z"/></svg>
  </div>

  <!-- Step titles -->
  <h3 class="step-title" style="left:65px;top:302px;">Scouting <span class="lower">and</span><br>Registering on<br>our website</h3>
  <h3 class="step-title" style="left:276px;top:302px;">The<br>First<br>Call</h3>
  <h3 class="step-title" style="left:486px;top:305px;">Matching</h3>
  <h3 class="step-title" style="left:697px;top:308px;">Recommendation<br>~ Client Interview</h3>
  <h3 class="step-title" style="left:913px;top:413px;">You<br>get the<br>job!</h3>
  <h3 class="step-title" style="left:1031px;top:413px;">You did<br>not get<br>the job!</h3>

  <!-- Step bodies -->
  <div class="step-body" style="left:65px;top:379px;">
    <p>Our fearless (but friendly!) recruiters will approach you on TalentNest if your profile looks like a match to one (or more!) of our jobs.</p>
    <p>You will be asked to register on our website, attach your CV and fill a quick skill sheet so we know what ac are great at.</p>
  </div>
  <div class="step-body" style="left:276px;top:379px;">
    <p>We will schedule a video call with you to go over your profile and understand your job hunting goals. You will be shown one or more jobs we think might be great for you!</p>
  </div>
  <div class="step-body" style="left:486px;top:379px;">
    <p>Behind the scenes, we keep<br>searching our jobs<br>database to find any opportunity<br>that might interest<br>and be suitable for you!</p>
  </div>
  <div class="step-body" style="left:697px;top:379px;">
    <p>Sit tight ~ once we get your blessing to proceed, we will send your profile and apply on your behalf for suitable jobs. We will be your ultimate cheerleaders to score some great interviews, and help you prepare once you get invited!</p>
  </div>
  <div class="step-body" style="left:913px;top:488px;width:95px;">
    <p class="outcome-lead">Congratulations!</p>
    <p>We'll help you review the offer letter and help you ensure a smooth start ;)</p>
  </div>
  <div class="step-body" style="left:1031px;top:488px;width:75px;">
    <p class="outcome-lead">No worries!</p>
    <p>We will keep sending you suitable jobs and help you prepare for the next great opportunity.</p>
  </div>

  <!-- Teams -->
  <div class="team" style="left:67px;top:548px;"><b>The TEAM:</b> A, B, C, D and E are our recruiters based in the Philippines</div>
  <div class="team" style="left:276px;top:548px;"><b>The TEAM:</b> F, G, H, I, J are our interviewers and they live everywhere ~ Japan, Australia, Malta, Indonesia... we truly are an international team!</div>
  <div class="team" style="left:697px;top:548px;"><b>The TEAM:</b>. K and L are our bilingual assistants, liaising between you and the clients and helping you get the most out of the interview. M, N and O are our Sales reps - they will negotiate with the client about your offer. They are based in Japan.</div>

  <!-- Illustrations -->
  <div class="illustration" role="img" aria-label="Faint illustration of a CV page with a headset-wearing recruiter avatar" style="left:180px;top:637px;width:64px;height:132px;background:linear-gradient(160deg,#e1e1e6,#e8e8ec);"></div>
  <div class="illustration" role="img" aria-label="Illustration of a person ticking off job cards on a checklist" style="left:446px;top:495px;width:232px;height:275px;background:linear-gradient(160deg,#e2e2e7,#e9e9ec);"></div>
  <div class="illustration" role="img" aria-label="Illustration of a video call window with three interview participants" style="left:853px;top:644px;width:191px;height:129px;background:linear-gradient(160deg,#dddde3,#e6e6ea);"></div>

  <!-- Tips -->
  <div class="tip" style="left:64px;top:652px;">
    <svg class="tip-badge" viewBox="0 0 34 28" aria-hidden="true"><path d="M4 2h24a3 3 0 0 1 3 3v13a3 3 0 0 1-3 3H14l-7 6v-6H4a3 3 0 0 1-3-3V5a3 3 0 0 1 3-3z" fill="var(--orange)"/><text x="16" y="15" text-anchor="middle" font-family="Roboto,Arial,sans-serif" font-size="9" font-weight="700" fill="#fff">TIP</text></svg>
    <div class="tip-text">Need a new CV?<br>Ask for our template!</div>
  </div>
  <div class="tip" style="left:276px;top:652px;">
    <svg class="tip-badge" viewBox="0 0 34 28" aria-hidden="true"><path d="M4 2h24a3 3 0 0 1 3 3v13a3 3 0 0 1-3 3H14l-7 6v-6H4a3 3 0 0 1-3-3V5a3 3 0 0 1 3-3z" fill="var(--orange)"/><text x="16" y="15" text-anchor="middle" font-family="Roboto,Arial,sans-serif" font-size="9" font-weight="700" fill="#fff">TIP</text></svg>
    <div class="tip-text" style="width:162px;">You can also ask us to recommend you auto matically to any job matching your skills and job preference. Leave it to us and increase your chances of scoring an interview!</div>
  </div>

  <div class="abs bottom-band"></div>
</main>
</body>
</html>
```